Creative & Professional Business Card for hair salon

We are looking to update our business cards. Our salon is creative, modern, progressive and professional and looking for a design that will reflect this.

```html
<!DOCTYPE html>
<html lang="en">
<head>
<meta charset="utf-8">
<title>Crown &amp; Mist – Business Card</title>
<link rel="stylesheet" href="https://fonts.googleapis.com/css2?family=Jost:wght@400;600&family=Yellowtail&display=swap">
<style>
  :root {
    --page-bg: #e9ebed;
    --card-front: #eef0f2;
    --card-border: #b8bcc0;
    --ink-blue: #3f7fab;
    --brand-blue: #6d9db3;
    --card-back: #4584ad;
    --white: #ffffff;
  }
  html, body {
    margin: 0;
    padding: 0;
    overflow: hidden;
  }
  .canvas {
    position: relative;
    width: 1200px;
    height: 1200px;
    background: var(--page-bg);
    overflow: hidden;
  }
  .card {
    position: absolute;
    left: 244px;
    width: 704px;
    height: 400px;
    box-sizing: border-box;
  }
  .card--front {
    top: 144px;
    background: var(--card-front);
    border: 2px solid var(--card-border);
  }
  .card--back {
    top: 652px;
    background: var(--card-back);
  }
  .contact-links {
    position: absolute;
    left: 44px;
    top: 36px;
    margin: 0;
    padding: 0;
    list-style: none;
    font-family: "Jost", sans-serif;
    font-weight: 600;
    font-size: 20px;
    line-height: 32px;
    color: var(--ink-blue);
  }
  .brand {
    position: absolute;
    left: 36px;
    top: 270px;
    display: flex;
    align-items: center;
    gap: 14px;
    font-family: "Jost", sans-serif;
    font-weight: 400;
    font-size: 40px;
    color: var(--brand-blue);
  }
  .brand__dot {
    width: 22px;
    height: 22px;
    border-radius: 50%;
    background: var(--brand-blue);
  }
  .address {
    position: absolute;
    left: 410px;
    top: 312px;
    margin: 0;
    font-family: "Jost", sans-serif;
    font-weight: 600;
    font-size: 15px;
    line-height: 36px;
    text-transform: uppercase;
    color: var(--ink-blue);
    font-style: normal;
  }
  .appointment__title {
    position: absolute;
    top: 54px;
    left: 0;
    width: 100%;
    margin: 0;
    text-align: center;
    font-family: "Yellowtail", cursive;
    font-weight: 400;
    font-size: 40px;
    color: var(--white);
  }
  .appointment__lines {
    position: absolute;
    left: 84px;
    top: 172px;
  }
</style>
</head>
<body>
<div class="canvas">
  <section class="card card--front">
    <ul class="contact-links">
      <li>hello@crownandmist.example</li>
      <li>www.crownandmist.example</li>
      <li>www.social.example/CrownAndMistStudio</li>
    </ul>
    <div class="brand">
      <span class="brand__dot"></span>
      <span class="brand__name">Crown &amp; Mist</span>
    </div>
    <address class="address">
      5/12 Harbour Lane, Maple Bay<br>
      PH 07 5550 1234
    </address>
  </section>

  <section class="card card--back">
    <h2 class="appointment__title">Your next appointment is:</h2>
    <svg class="appointment__lines" width="556" height="172" viewBox="0 0 556 172">
      <g stroke="#ffffff" stroke-width="2">
        <line x1="0" y1="2" x2="556" y2="2"/>
        <line x1="0" y1="58" x2="556" y2="58"/>
        <line x1="0" y1="114" x2="556" y2="114"/>
        <line x1="0" y1="170" x2="556" y2="170"/>
      </g>
    </svg>
  </section>
</div>
</body>
</html>
```